Corvantis websites redesign

Www.cor-vantis.com needs to be redesigned along with updations. The incremental material will be provided for the updations. We are looking for complete redesign of the pages with the new content. The complete write up will be provided soon

Target Market(s)

Global

Coding

Coded - Design and coding required

Number of Pages Required

5+ page

Requirements
Must have
• A clean and slick design for the Consulting.
Should not have
• Too many pictures which reduces the speed of the site

```html
<!DOCTYPE html>
<html lang="en">
<head>
<meta charset="utf-8">
<title>Corvantis – Our Expertise</title>
<link rel="stylesheet" href="https://fonts.googleapis.com/css2?family=Jost:wght@300;400;500;600&display=swap">
<style>
:root{
  --white:#ffffff;
  --nav-active:#1d7fa8;
  --nav:#6b1e2a;
  --brand:#33324f;
  --accent:#3aa6d6;
  --accent-text:#0d2a3a;
  --hero-text:#f2f5f8;
  --footer:#0f1f2b;
  --footer-text:#9aa6b0;
}
*{margin:0;padding:0;box-sizing:border-box}
html,body{width:1200px;height:894px;overflow:hidden;background:var(--white)}
body{font-family:"Jost",sans-serif;color:var(--hero-text);position:relative}
.site-header{position:absolute;left:0;top:0;width:1200px;height:120px;background:var(--white)}
.brand{position:absolute;left:58px;top:42px;display:flex;align-items:center;gap:12px}
.brand-dot{width:30px;height:30px;border-radius:50%;background:var(--brand)}
.brand-name{font-size:36px;font-weight:400;color:var(--brand);letter-spacing:.5px}
.main-nav{position:absolute;right:80px;top:58px;display:flex;gap:27px}
.main-nav a{text-decoration:none;font-size:17px;font-weight:500;color:var(--nav);letter-spacing:.3px}
.main-nav a.active{color:var(--nav-active)}
.hero{position:absolute;left:0;top:120px;width:1200px;height:714px}
.hero-photo{position:absolute;inset:0;background:linear-gradient(120deg,#1f3142 0%,#3e5366 38%,#6f7f8c 62%,#4a5c6c 82%,#2a3c4c 100%)}
.hero-content{position:absolute;inset:0}
.page-title{position:absolute;left:55px;top:46px;font-size:38px;font-weight:300;letter-spacing:.5px}
.text{position:absolute;font-size:13px;line-height:17px;font-weight:400}
.text strong{font-weight:600}
.tag{position:absolute;height:46px;background:var(--accent);color:var(--accent-text);font-size:14px;display:flex;align-items:center;padding-left:27px;letter-spacing:.2px}
.item{position:absolute;display:flex;gap:8px;font-size:12px;line-height:14px}
.item .num{font-size:30px;font-weight:600;line-height:30px;color:#1a1a1a;-webkit-text-stroke:0}
.item small{font-size:9px;line-height:13px;display:block}
.site-footer{position:absolute;left:0;top:834px;width:1200px;height:60px;background:var(--footer)}
.copyright{position:absolute;right:82px;top:23px;font-size:11px;font-weight:500;color:var(--footer-text)}
</style>
</head>
<body>
<header class="site-header">
  <div class="brand"><span class="brand-dot"></span><span class="brand-name">Corvantis</span></div>
  <nav class="main-nav">
    <a class="active" href="#">HOME</a>
    <a href="#">FOUNDER</a>
    <a href="#">CONSULTANCY</a>
    <a href="#">SYSTEM</a>
    <a href="#">CASE STUDIES</a>
    <a href="#">CONTACT</a>
  </nav>
</header>

<main class="hero">
  <div class="hero-photo" role="img" aria-label="Background photo of a businessman signing documents at a desk"></div>
  <div class="hero-content">
    <h1 class="page-title">OUR EXPERTISE</h1>
    <p class="text" style="left:53px;top:226px;width:520px">CCL will work with you to understand your business and offer need based strategic and transactional advice which fits your corporate strategy. There are no standard solutions and every situation might be different requiring a different approach, so please give us a chance to understand your requirements and contact us for a discussion.</p>

    <div class="tag" style="left:52px;top:336px;width:418px">CONSULTANCY - PLAIN VANILLA FINANCING SOLUTIONS</div>
    <p class="text" style="left:53px;top:404px;width:505px">The Consultancy provides access to local/regional banks across <strong>Hong Kong, Singapore, Dubai , New York and London</strong> and helps corporate clients in diversifying their financial partners and adding new banks to their bank group. The Consultancy provides Trade finance solutions for working capital requirements and assists in arranging External Commercial Borrowings/Foreign Currency Term Loans for long-term requirements.</p>
    <p class="text" style="left:52px;top:519px">Our main areas of expertise:</p>

    <div class="item" style="left:50px;top:548px;width:190px"><span class="num">1</span><span>Introduction of regional bank for Subsidiaries /Joint Ventures across the world</span></div>
    <div class="item" style="left:246px;top:548px;width:225px"><span class="num">2</span><span>Plain-vanilla working capital lines from banks – Letter of Credit, Trust Receipt, Bill Discounting, etc</span></div>
    <div class="item" style="left:50px;top:630px;width:195px"><span class="num">3</span><span>Arranging External Commercial Borrowings / Foreign Currency Term Loans for long-term requirement</span></div>
    <div class="item" style="left:251px;top:630px;width:190px"><span class="num">4</span><span>Providing efficiency in terms of better leverage and pricing through new lenders</span></div>
    <div class="item" style="left:452px;top:622px;width:135px"><span class="num">5</span><span>Bank line business like Guarantee issuance and LC confirmations over longer tenor</span></div>

    <div class="tag" style="left:617px;top:228px;width:418px">CONSULTANCY - STRUCTURED FINANCING SOLUTIONS</div>
    <p class="text" style="left:613px;top:307px;width:512px">The Consultancy provides end-to-end structured solutions on the Payables, Receivables or Inventory side for working capital requirements with off/part/on recourse balance sheet structures. We also specialize in providing credit enhancements through private or sovereign Insurance market to enhance the rating of a debt paper and improve distribution and market appetite.</p>
    <p class="text" style="left:613px;top:408px;width:512px">On the term side, the Consultancy focuses on providing access to alternate liquidity providers like Developmental Financial Institutions, Export Credit Agency and Hedge Funds for both corporates and banks<br>The Consultancy through varied structure can also assist in monetization of unfunded bank lines for arranging financing.</p>
    <p class="text" style="left:616px;top:508px">Our main areas of expertise:</p>

    <div class="item" style="left:617px;top:548px;width:200px"><span class="num">1</span><span>Structured working capital solutions – like back-to-back LC, front-to-back LC, etc.</span></div>
    <div class="item" style="left:874px;top:548px;width:190px"><span class="num">2</span><span>Recourse/ part recourse/ non-recourse receivables financing – with or without credit enhancements</span></div>
    <div class="item" style="left:617px;top:626px;width:240px"><span class="num">3</span><span>Export prepayments - Pre-export unsecured advance against contracts /open account/LC with the Buyers.<small>This significantly reduces the working capital utilisation of most companies</small></span></div>
    <div class="item" style="left:876px;top:618px;width:280px"><span class="num">4</span><span><small>Structured project financing through Export Credit Agencies and Developmental Financial Institutions -</small>Direct credit limit on the projects can be looked into either with a single DFI or with a consortium of ECA/DFI's which makes the project significantly scalable</span></div>
  </div>
</main>

<footer class="site-footer">
  <p class="copyright">© CORVANTIS CONSULTANCY LIMITED</p>
</footer>
</body>
</html>
```